Double Sided Business Card Design for Pet Services

My mom and I want to start a business for pets. We want to offer dog walking, pet sitting as well as boarding and grooming at our home. For the front of the business card, we want a logo that will capture all of our services. We want the name to be Morrito, Inc., which means little paws in Spanish. Perhaps, there could be little paws or just a little paw implemented within the word Morrito. Or we would want a cat and a dog by the word Morrito. We have a cat and a dog at home, and we would be really happy if they could be a part of the business card. It does not have to be anything crazy. Just an outline of a cat or a dog would be awesome. Please see uploaded file.
As for the back of the card, we would want little paws all over the card or we would want a collar, leash, grooming scissor, dog/cat bowl, bone, fish, or toy to show all of the services that we provide. Along with either the many paws or many pet objects, we would want to add our information, such as name (Rosalba Ferrin), telephone numbers (512) 876-2093, e-mail addresses morritoinc@bramwel.com, etc.
We would also want a catch phrase to go on the back of the card, such as "Where all paws matter!" Or "We strive for happy tails." or "A paw-bulous service is guaranteed!"
As for colors, we would not want that many. We would want perhaps white and blue. We would want soft colors that will stand out and make an impression. The same goes with the text. An elegant text would be nice. Or perhaps a text with bold letters. We are excited to see the results, but we are also excited to see your creative ideas and what you will bring to the table.

Target Market(s)

Pet Owners

Contact Information for Business Card

For the front of the business card, we want a logo that will capture all of our services. We want the name to be Morrito, Inc., which means little paws in Spanish. Perhaps, there could be little paws or just a little paw implemented within the word Morrito. Or we would want a cat and a dog by the word Morrito. We have a cat and a dog at home, and we would be really happy if they could be a part of the business card. It does not have to be anything crazy. Just an outline of a cat or a dog would be awesome. Please see uploaded file.
As for the back of the card, we would want little paws all over the card or we would want a collar, leash, grooming scissor, dog/cat bowl, bone, fish, or toy to show all of the services that we provide. Along with either the many paws or many pet objects, we would want to add our information, such as name, telephone numbers, e-mail addresses, etc. We would also want a catch phrase to go on the back of the card, such as "Where all paws matter!" Or "We strive happy tails." or "A paw-bulous service is guaranteed!" Or if there is a way to put the catch phrase in the front of the card. We are open to seeing variety.

Logo Text

Morrito, Inc

Font styles to use
Serif
Script

Colors
ffffff
33a6d7
145ea8

Requirements
Must have
• My project must be a double sided business card.

```html
<!DOCTYPE html>
<html lang="en">
<head>
<meta charset="utf-8">
<title>Morrito, Inc. — Business Card</title>
<link rel="stylesheet" href="https://fonts.googleapis.com/css2?family=Kaushan+Script&family=Rye&family=Special+Elite&display=swap">
<style>
  :root{
    --stage:#dcdcdf;
    --card-blue:#33a6d7;
    --pattern-blue:#2f9bcc;
    --ink-blue:#145ea8;
    --white:#ffffff;
    --card-w:760px;
    --card-h:400px;
    --radius:30px;
  }
  *{margin:0;padding:0;box-sizing:border-box;}
  html,body{width:1200px;height:1200px;overflow:hidden;}
  body{background:var(--stage);position:relative;}

  .card{
    position:absolute;
    left:220px;
    width:var(--card-w);
    height:var(--card-h);
    border-radius:var(--radius);
    overflow:hidden;
    background:var(--card-blue);
  }
  .card--front{top:150px;}
  .card--back{top:650px;}

  .card__pattern{
    position:absolute;inset:0;
    background:linear-gradient(135deg,var(--card-blue),var(--pattern-blue));
  }

  .brand-name{
    position:absolute;
    font-family:"Kaushan Script",cursive;
    font-weight:400;
    line-height:1;
    white-space:nowrap;
  }
  .card--front .brand-name{
    left:170px;top:92px;
    font-size:136px;
    color:var(--white);
  }
  .card--back .brand-name{
    left:210px;top:66px;
    font-size:118px;
    color:var(--ink-blue);
  }

  .holder{
    position:absolute;
    left:44px;top:282px;
    font-family:"Rye",serif;
    color:var(--ink-blue);
    font-size:24px;
    line-height:1.05;
    text-transform:uppercase;
  }

  .contact-list{
    position:absolute;
    left:380px;top:270px;
    list-style:none;
    font-family:"Special Elite",monospace;
    color:var(--ink-blue);
    font-size:20px;
    font-style:italic;
  }
  .contact-list__item{
    display:flex;align-items:center;gap:14px;
    height:30px;
  }
  .contact-list__icon{width:18px;height:18px;flex:none;}
</style>
</head>
<body>

  <section class="card card--front" aria-label="Card front">
    <div class="card__pattern" role="img" aria-label="Repeating pattern of outlined cat and dog faces in soft blue"></div>
    <div class="brand-name">Morrito</div>
  </section>

  <section class="card card--back" aria-label="Card back">
    <div class="card__pattern" role="img" aria-label="Repeating pattern of outlined cat and dog faces in soft blue"></div>
    <div class="brand-name">Morrito</div>

    <div class="holder">
      <div class="holder__name">Rosalba Ferrin</div>
      <div class="holder__role">Position</div>
    </div>

    <ul class="contact-list">
      <li class="contact-list__item">
        <svg class="contact-list__icon" viewBox="0 0 20 20" fill="none" stroke="#145ea8" stroke-width="1.6"><rect x="2" y="4" width="16" height="12" rx="1"/><path d="M2 5l8 6 8-6"/></svg>
        <span>morritoinc@bramwel.com</span>
      </li>
      <li class="contact-list__item">
        <svg class="contact-list__icon" viewBox="0 0 20 20" fill="none" stroke="#145ea8" stroke-width="1.6"><path d="M5 2.5l3 3.5-2 2c1 2.5 3 4.5 5.5 5.5l2-2 3.5 3-2 2.5C9 16.5 3.5 11 2.5 5z"/></svg>
        <span>(512) 876-2093</span>
      </li>
      <li class="contact-list__item">
        <svg class="contact-list__icon" viewBox="0 0 20 20" fill="none" stroke="#145ea8" stroke-width="1.6"><path d="M10 18s-6-6-6-10a6 6 0 0 1 12 0c0 4-6 10-6 10z"/><circle cx="10" cy="8" r="2.2"/></svg>
        <span>AUSTIN, TX</span>
      </li>
      <li class="contact-list__item">
        <svg class="contact-list__icon" viewBox="0 0 20 20" fill="none" stroke="#145ea8" stroke-width="1.6"><circle cx="10" cy="10" r="8"/><ellipse cx="10" cy="10" rx="3.5" ry="8"/><path d="M2 10h16"/></svg>
        <span>www.morritoinc.com</span>
      </li>
    </ul>
  </section>

</body>
</html>
```